This book will apply the 12 Steps to gaming addiction, also known as video game addiction. The primary purpose of the book is to provide an effective solution for this new type of addiction. The solution is based on the rich and successful concepts of traditional twelve-step programs like RL.

The title on the cover will be "Nine Doors Past the Glowing Screen" and "by Martin Quorby". A subtitle can be used if it works in your design of "A Practical Path Beyond Compulsive Console Play". Cover will be for a 6" x 9" book approximately 110 pages in length.

Some back cover text including some review quotes and an author bio are in the attached Word doc. There is also an author photo attached for for the back cover.

Requirements
Must have
• For the cover design it could be stylized, or an image, a partial image, or whatever. I am open to suggestions. Think about what would be noticed by a person searching for help with moderating their video game use, or by the parents or loved ones of problem gamers. Something contemporary and eye catching.

```html
<!DOCTYPE html>
<html lang="en">
<head>
<meta charset="utf-8">
<title>Nine Doors Past the Glowing Screen — Martin Quorby</title>
<link rel="stylesheet" href="https://fonts.googleapis.com/css2?family=Mouse+Memoirs&display=swap">
<style>
  :root {
    --page-bg: #ffffff;
    --cover-light: #e6e4e5;
    --cover-mid: #d8d6d7;
    --ink: #141414;
    --art-top: #3a3a3a;
    --art-bottom: #1c1c1c;
    --accent-blue: #4a6b9c;
  }
  html, body {
    margin: 0;
    padding: 0;
    width: 1200px;
    height: 960px;
    overflow: hidden;
    background: var(--page-bg);
  }
  .book-cover {
    position: absolute;
    left: 310px;
    top: 30px;
    width: 580px;
    height: 900px;
    background: linear-gradient(120deg, var(--cover-light) 0%, var(--cover-mid) 100%);
    overflow: hidden;
    font-family: "Mouse Memoirs", "Arial Narrow", sans-serif;
    color: var(--ink);
    text-transform: uppercase;
  }
  .cover-artwork {
    position: absolute;
    left: 26px;
    top: 0;
    width: 140px;
    height: 900px;
    background: linear-gradient(180deg, var(--art-top) 0%, var(--art-bottom) 100%);
    opacity: 0.85;
  }
  .cover-subtitle {
    position: absolute;
    left: 186px;
    top: 64px;
    width: 330px;
    margin: 0;
    font-size: 40px;
    line-height: 1;
    font-weight: 400;
    text-align: center;
    letter-spacing: 0.5px;
  }
  .cover-subtitle .accent { color: var(--accent-blue); }
  .cover-title {
    position: absolute;
    right: 80px;
    top: 196px;
    margin: 0;
    font-weight: 400;
    text-align: right;
    line-height: 0.84;
  }
  .cover-title .title-line { display: block; }
  .cover-title .title-line--lead { font-size: 116px; }
  .cover-title .title-line--main { font-size: 94px; }
  .cover-title .title-line--accent {
    font-size: 100px;
    color: var(--accent-blue);
  }
  .cover-author {
    position: absolute;
    right: 86px;
    top: 772px;
    margin: 0;
    font-size: 54px;
    line-height: 0.9;
    font-weight: 400;
    text-align: left;
  }
</style>
</head>
<body>
  <main class="book-cover">
    <div class="cover-artwork" role="img" aria-label="Illustration: black handcuff chained to a game controller"></div>

    <p class="cover-subtitle">A Practical Path Beyond<br><span class="accent">Compulsive Console Play</span></p>

    <h1 class="cover-title">
      <span class="title-line title-line--lead">Nine</span>
      <span class="title-line title-line--main">Doors</span>
      <span class="title-line title-line--main">Past the</span>
      <span class="title-line title-line--accent">Glowing</span>
      <span class="title-line title-line--accent">Screen</span>
    </h1>

    <p class="cover-author">Martin<br>Quorby</p>
  </main>
</body>
</html>
```